Financial Advisor Business Card

This business card is mainly a card for me personally (Marcus Pellinger) providing services as a Financial Planner and Accountant. My title is: Worth.wise Planner
Details provided about Harbour Financial Planners on the reverse side of the card is not dominant information, it is provided for ease of contact/communication purposes for prospective clients.
About me: I provide financial advice to my clients however due to regulatory issues in my industry I cannot use the title "Financial Advisor".
Target market is 25 y/o and onwards projecting a cutting edge, innovative and modern marketing influence.
Target Market(s)
25 years old and older
Industry/Entity Type
Financial
Contact Information for Business Card
Front side of business card
Name: Marcus Pellinger
Position: Worth.wise Planner
Accreditations:
Dip FS(FP)
B.Comm
Mobile: 0438 702 519
e-mail: mp@harbourfp.example.au
website: www.harbourfp.example.au
Reverse side of business card
Name: Marcus Pellinger
Company: Harbour Financial Planners
Position: Senior Accountant
Address:
Level 6, Suite 4
47 Orwell Road
PO Box 817
MERRIVALE NSW 2315
Phone: (02) 49581737
Requirements
Must have
- - Cutting edge, innovative, fun but professional, modern marketing design and fonts
- Professional and legible
- Futuristic sharp lines, some with rounded edges
- Preferred Front Card colour scheme: Black background, Silver Text, White Text, Red & Silver lines
- Preferred Reverse Card colour scheme: White background, Silver Text, Black Text, Aqua & Silver lines
Nice to have
- Design a cutting edge logo of my intials as capital letters: MP
with a bigger D and smaller K - Preferred colour is Silver Text
Should not have
- Must not be:
- vintage/classic
- stereotypical accountant/tax agent/money style business card
- old style fonts e.g. times new roman

```html
<!DOCTYPE html>
<html lang="en">
<head>
<meta charset="utf-8">
<title>Marcus Pellinger – Business Card</title>
<link rel="stylesheet" href="https://fonts.googleapis.com/css2?family=Open+Sans:wght@300;400;700&display=swap">
<style>
  :root {
    --backdrop: #ece9e4;
    --card-white: #ffffff;
    --red-deep: #7e0f17;
    --red-main: #b3212b;
    --red-bright: #c8303a;
    --ink: #3a3a3a;
    --silver: #d9d9d9;
    --silver-dark: #a9a9a9;
  }
  * { box-sizing: border-box; margin: 0; padding: 0; }
  html, body {
    width: 1200px; height: 1024px; overflow: hidden;
    background: var(--backdrop);
    font-family: "Open Sans", Arial, sans-serif;
  }
  .stage { position: relative; width: 1200px; height: 1024px; }

  /* Front card */
  .card-front {
    position: absolute; left: 60px; top: 318px;
    width: 660px; height: 378px;
    background: var(--card-white);
    box-shadow: 0 10px 30px rgba(0,0,0,.18);
    overflow: hidden;
  }
  .card-front .monogram {
    position: absolute; left: 58px; top: 150px;
    font-weight: 300; font-size: 150px; line-height: 1;
    color: var(--red-main); letter-spacing: -4px;
  }
  .card-front .divider {
    position: absolute; left: 322px; top: 70px;
    width: 2px; height: 190px;
    background: linear-gradient(to bottom, rgba(126,15,23,0), var(--red-deep) 55%, rgba(126,15,23,0));
  }
  .card-front .details {
    position: absolute; left: 356px; top: 84px;
    color: var(--ink); font-size: 14px; line-height: 1.5;
  }
  .details .name { color: var(--red-main); font-weight: 700; font-size: 17px; }
  .details .contact { margin-top: 10px; list-style: none; }
  .details .contact li { display: flex; align-items: center; gap: 8px; }
  .details .contact svg { width: 13px; height: 13px; flex: none; }
  .card-front .band {
    position: absolute; left: 0; bottom: 0; width: 100%; height: 22px;
    background: linear-gradient(to right, var(--red-deep), var(--red-bright) 60%, var(--red-main));
  }

  /* Back card */
  .card-back {
    position: absolute; left: 790px; top: 222px;
    width: 350px; height: 600px;
    background: linear-gradient(160deg, var(--red-deep) 0%, var(--red-bright) 45%, var(--red-main) 75%, var(--red-deep) 100%);
    box-shadow: 0 10px 30px rgba(0,0,0,.25);
    overflow: hidden;
  }
  .card-back .monogram {
    position: absolute; left: 78px; top: 170px;
    font-weight: 300; font-size: 170px; line-height: 1;
    color: var(--silver); letter-spacing: -4px;
  }
  .card-back .web {
    position: absolute; left: 40px; top: 300px;
    transform-origin: left top; transform: rotate(90deg) translate(-50%, 0);
    color: var(--silver); font-size: 17px; white-space: nowrap;
  }
</style>
</head>
<body>
<main class="stage">
  <section class="card-front" aria-label="Card front">
    <div class="monogram">MP</div>
    <div class="divider"></div>
    <div class="details">
      <p class="name">Marcus Pellinger</p>
      <p class="title">Worth.wise Planner</p>
      <p class="credentials">Dip FS(FP) | B.Comm</p>
      <ul class="contact">
        <li>
          <svg viewBox="0 0 12 12" aria-hidden="true"><rect x="2.5" y="0.5" width="7" height="11" rx="1" fill="none" stroke="#b3212b"/><circle cx="6" cy="9.5" r=".8" fill="#b3212b"/></svg>
          0438 702 519
        </li>
        <li>
          <svg viewBox="0 0 12 12" aria-hidden="true"><rect x="0.5" y="2" width="11" height="8" fill="#b3212b"/><path d="M1 2.5 6 6.5 11 2.5" fill="none" stroke="#fff"/></svg>
          mp@harbourfp.example.au
        </li>
        <li>
          <svg viewBox="0 0 12 12" aria-hidden="true"><circle cx="6" cy="6" r="5.5" fill="#b3212b"/><path d="M.5 6h11M6 .5c-3 3-3 8 0 11M6 .5c3 3 3 8 0 11" fill="none" stroke="#fff" stroke-width=".8"/></svg>
          www.harbourfp.example.au
        </li>
      </ul>
    </div>
    <div class="band"></div>
  </section>

  <section class="card-back" aria-label="Card back">
    <div class="monogram">MP</div>
    <p class="web">www.harbourfp.example.au</p>
  </section>
</main>
</body>
</html>
```